"Orvane Community Supports" Business Card Design

We are a not for profit disability service that has recently changed its logo and trading name and is in the process of "rebranding".We provide employment, training and accommodation to people with disabilities. We find our new logo fresh and inspiring and would like our new business cards to reflect the same feeling. Our marketing line is "Growth, Opportunity, Empowerment".

Target Market(s)

People with disabilities and their families, carers, support network

Industry/Entity Type

Business

Contact Information for Business Card

NamePositionAddressHead OfficeDirect LineMobileFaxEmailWebsite

Requirements
Must have
• Our logo; space for the above listed information requirements

```html
<!DOCTYPE html>
<html lang="en">
<head>
<meta charset="utf-8">
<title>Orvane – Business Card</title>
<link href="https://fonts.googleapis.com/css2?family=Lato:wght@400;700&display=swap" rel="stylesheet">
<style>
  :root {
    --page-bg: #d9d7d4;
    --lime-light: #c3dd2f;
    --lime-mid: #a9cd35;
    --lime-deep: #8fbf3a;
    --panel: #b4d63a;
    --line: rgba(90, 120, 30, 0.45);
    --white: #ffffff;
    --tag-blue: #2a7fc0;
    --icon-blue: #2b6aa8;
  }
  * { box-sizing: border-box; margin: 0; padding: 0; }
  html, body {
    width: 1200px; height: 1000px; overflow: hidden;
    background: var(--page-bg);
    font-family: "Lato", Arial, sans-serif;
  }
  .business-card {
    position: absolute; left: 150px; top: 240px;
    width: 900px; height: 520px;
    overflow: hidden;
    background: radial-gradient(ellipse at 40% 55%, var(--lime-light) 0%, var(--lime-mid) 55%, var(--lime-deep) 100%);
    box-shadow: 0 10px 30px rgba(0,0,0,0.18);
  }
  .card-shapes { position: absolute; inset: 0; }
  .holder { position: absolute; left: 72px; top: 170px; color: var(--white); }
  .holder-name { font-size: 24px; font-weight: 400; }
  .holder-position { font-size: 15px; margin-top: 4px; }
  .contact-list { position: absolute; left: 72px; list-style: none; color: var(--white); font-size: 15px; }
  .contact-list li { display: flex; align-items: center; gap: 10px; height: 24px; }
  .contact-phone { top: 300px; }
  .contact-web { top: 395px; }
  .contact-icon {
    width: 18px; height: 18px; border-radius: 3px;
    background: var(--white); display: flex; align-items: center; justify-content: center;
  }
  .contact-icon svg { width: 12px; height: 12px; fill: var(--icon-blue); }
  .brand {
    position: absolute; left: 480px; top: 130px; width: 320px;
    color: var(--white);
  }
  .brand-name { display: flex; align-items: center; gap: 14px; font-size: 72px; font-weight: 700; line-height: 1; letter-spacing: 2px; }
  .brand-dot { width: 40px; height: 40px; border-radius: 50%; background: var(--white); flex: none; }
  .brand-sub { margin-top: 4px; margin-left: 54px; font-size: 18px; font-weight: 400; }
  .brand-tagline { margin-top: 4px; margin-left: 54px; color: var(--tag-blue); font-size: 16px; }
</style>
</head>
<body>
  <article class="business-card">
    <svg class="card-shapes" viewBox="0 0 900 520" aria-hidden="true">
      <polygon points="430,60 830,0 900,0 900,520 470,520" fill="rgba(255,255,255,0.05)"/>
      <polygon points="420,95 820,55 860,420 460,470" fill="var(--panel)" stroke="var(--line)" stroke-width="1"/>
      <line x1="690" y1="0" x2="900" y2="75" stroke="var(--line)" stroke-width="1"/>
      <line x1="860" y1="420" x2="900" y2="370" stroke="var(--line)" stroke-width="1"/>
      <line x1="460" y1="470" x2="560" y2="520" stroke="var(--line)" stroke-width="1"/>
    </svg>

    <div class="holder">
      <p class="holder-name">Name : Sample Text</p>
      <p class="holder-position">Position</p>
    </div>

    <ul class="contact-list contact-phone">
      <li><span class="contact-icon"><svg viewBox="0 0 12 12"><path d="M2 1h3l1 3-1.5 1a6 6 0 0 0 2.5 2.5L8 6l3 1v3a1 1 0 0 1-1 1A9 9 0 0 1 1 2a1 1 0 0 1 1-1z"/></svg></span>Direct Line</li>
      <li><span class="contact-icon"><svg viewBox="0 0 12 12"><rect x="3" y="0.5" width="6" height="11" rx="1"/></svg></span>Mobile</li>
      <li><span class="contact-icon"><svg viewBox="0 0 12 12"><rect x="1" y="4" width="10" height="6" rx="1"/><rect x="3" y="1" width="6" height="3"/></svg></span>Fax</li>
    </ul>

    <ul class="contact-list contact-web">
      <li><span class="contact-icon"><svg viewBox="0 0 12 12"><path d="M6 0.5a4 4 0 0 1 4 4c0 3-4 7-4 7s-4-4-4-7a4 4 0 0 1 4-4z"/></svg></span>AddressHead Office</li>
      <li><span class="contact-icon"><svg viewBox="0 0 12 12"><rect x="0.5" y="2" width="11" height="8" rx="1"/></svg></span>Email</li>
      <li><span class="contact-icon"><svg viewBox="0 0 12 12"><circle cx="6" cy="6" r="5"/></svg></span>Website</li>
    </ul>

    <div class="brand">
      <p class="brand-name"><span class="brand-dot"></span>ORV</p>
      <p class="brand-sub">orvane services</p>
      <p class="brand-tagline">Learn, Work, Belong, Thrive.</p>
    </div>
  </article>
</body>
</html>
```